KESTREL Communications Business Card- Belsa

Kestrel Integrated Communications is Corporate communications agency with more than 20 years of experience. We become part of the manegement team of our clients in other to improve their outcomes and grow the possitioning of their brand.
We are in Puerto Rico, latin caribbean island
Name: Maribelsa (Belsa) Ocampo
787-555-0148
bocampo@kestrelwing.example

Target Market(s)

finance and pharmaceutical companies

Industry/Entity Type

Business

Contact Information for Business Card

modern, edgy colorful and playfull like our logo

Requirements
Must have
• company logo
• name
• tel
• email

```html
<!DOCTYPE html>
<html lang="en">
<head>
<meta charset="utf-8">
<title>KESTREL Communications – Business Card – Belsa</title>
<link rel="stylesheet" href="https://fonts.googleapis.com/css2?family=Open+Sans:wght@400;600;700&display=swap">
<style>
  :root {
    --backdrop: #e7e3dd;
    --card-ink: #242122;
    --accent-orange: #f2601e;
    --paper-white: #ffffff;
    --soft-white: #f1f1f1;
    --card-shadow: rgba(0, 0, 0, 0.28);
  }
  * { box-sizing: border-box; margin: 0; padding: 0; }
  html, body {
    width: 1200px;
    height: 1200px;
    overflow: hidden;
    background: var(--backdrop);
    font-family: "Open Sans", Arial, sans-serif;
  }
  .canvas {
    position: relative;
    width: 1200px;
    height: 1200px;
    display: flex;
    flex-direction: column;
    align-items: center;
    justify-content: center;
    gap: 36px;
  }
  .card {
    position: relative;
    width: 900px;
    height: 514px;
    background: var(--card-ink);
    box-shadow: 0 10px 28px var(--card-shadow);
    overflow: hidden;
  }

  /* Back side: centred wordmark */
  .card-back {
    display: flex;
    align-items: center;
    justify-content: center;
  }
  .brand-lockup {
    display: flex;
    align-items: center;
    gap: 18px;
  }
  .brand-mark {
    width: 22px;
    height: 22px;
    background: var(--accent-orange);
  }
  .brand-name {
    font-weight: 700;
    color: var(--paper-white);
    letter-spacing: 0.08em;
    line-height: 1;
  }
  .card-back .brand-name { font-size: 88px; }

  /* Front side: large wordmark at left, contact at right */
  .card-front .brand-lockup {
    position: absolute;
    left: 40px;
    top: 150px;
  }
  .card-front .brand-name { font-size: 104px; }
  .card-front .brand-mark { width: 26px; height: 26px; }

  .contact-block {
    position: absolute;
    left: 520px;
    top: 330px;
    color: var(--soft-white);
  }
  .person-name {
    font-size: 27px;
    font-weight: 400;
    color: var(--accent-orange);
    margin-bottom: 30px;
    white-space: nowrap;
  }
  .person-name .nickname { color: var(--paper-white); }
  .contact-line {
    display: flex;
    align-items: center;
    gap: 14px;
    font-size: 20px;
    line-height: 1.55;
    white-space: nowrap;
  }
  .contact-icon { width: 20px; height: 16px; flex: none; }
</style>
</head>
<body>
<main class="canvas">

  <section class="card card-back" aria-label="Business card, back">
    <div class="brand-lockup">
      <span class="brand-mark" aria-hidden="true"></span>
      <span class="brand-name">KESTREL</span>
    </div>
  </section>

  <section class="card card-front" aria-label="Business card, front">
    <div class="brand-lockup">
      <span class="brand-mark" aria-hidden="true"></span>
      <span class="brand-name">KESTREL</span>
    </div>

    <div class="contact-block">
      <p class="person-name">Maribelsa (<span class="nickname">Belsa</span>) Ocampo</p>
      <p class="contact-line">
        <svg class="contact-icon" viewBox="0 0 20 16" aria-hidden="true">
          <path fill="#f2601e" d="M2 5c0-2 3-4 8-4s8 2 8 4v1.5h-4V5c0-.6-2-1-4-1S6 4.4 6 5v1.5H2z"/>
          <path fill="#f2601e" d="M5 8h10l2 7H3z"/>
          <circle cx="10" cy="11.5" r="1.8" fill="#242122"/>
        </svg>
        <span class="contact-phone">787-555-0148</span>
      </p>
      <p class="contact-line">
        <svg class="contact-icon" viewBox="0 0 20 16" aria-hidden="true">
          <rect x="1" y="2" width="18" height="12" fill="#f2601e"/>
          <path d="M1.5 2.5 10 9l8.5-6.5" fill="none" stroke="#242122" stroke-width="1.6"/>
        </svg>
        <span class="contact-email">bocampo@kestrelwing.example</span>
      </p>
    </div>
  </section>

</main>
</body>
</html>
```